Packaging Design for Peach Halves in Syrup

Hello Designer,
We have to create a packaging design for a peach halves in syrup product.
The design should be eye-catching, appealing to the target europeen market, and convey the product's quality and freshness.
Peach halves in syrup, packed in glass jars with yellow lids. The jar size is as a picture attached below.
Logo : MOLAN
Label Design: Design a label that prominently features the product name in english and french, "Peach Halves in Syrup," "Pêches en moitiés" and highlights key selling points such as "100% Natural" or "No Added Preservatives."
Visual Elements: Incorporate image or illustration of ripe peaches to emphasize the product's freshness and natural ingredients.
Color Scheme: Use a color scheme that complements the yellow lids, making the product stand out on the shelf. Consider using warm, inviting colors to evoke the feeling of freshness.

Nutritional Information: Include a panel for nutritional information.
ingredients list -Eng : peaches, water, Sugar.
-Fr : pêches, eau, sucre.
Barcode: leave a space for barcode.

Target Market(s)

Europe

Font styles to use
Serif
Decorative
Script

Requirements
Must have
• -Product name : ENG and FR, barcode, nutritional information, ingredients : Eng and French.

```html
<!DOCTYPE html>
<html lang="en">
<head>
<meta charset="utf-8">
<title>MOLAN Peach Halves in Syrup – Jar Label</title>
<link rel="stylesheet" href="https://fonts.googleapis.com/css2?family=Fredoka:wght@500;600&family=Kaushan+Script&family=Roboto:wght@500;700&display=swap">
<style>
  :root {
    --label-red: #e21030;
    --arch-yellow: #ecd81f;
    --brand-navy: #2d2b6e;
    --panel-grey: #d9d9d9;
    --badge-green: #1f9a3a;
    --white: #ffffff;
    --page-bg: #ffffff;
    --peach-light: #fbd27a;
    --peach-mid: #f59a3c;
    --peach-deep: #e2432c;
  }
  * { margin: 0; padding: 0; box-sizing: border-box; }
  html, body {
    width: 1200px;
    height: 1200px;
    overflow: hidden;
    background: var(--page-bg);
  }
  .canvas {
    position: relative;
    width: 1200px;
    height: 1200px;
  }
  .label {
    position: absolute;
    left: 40px;
    top: 428px;
    width: 1120px;
    height: 343px;
    background: var(--label-red);
    overflow: hidden;
    font-family: "Roboto", Arial, sans-serif;
  }
  .front-arch {
    position: absolute;
    left: 112px;
    top: 21px;
    width: 327px;
    height: 322px;
    background: var(--arch-yellow);
    border-radius: 164px 164px 0 0;
  }
  .peach-visual {
    position: absolute;
    left: 327px;
    top: 17px;
    width: 349px;
    height: 326px;
    border-radius: 48% 52% 40% 60% / 55% 50% 50% 45%;
    background:
      radial-gradient(circle at 52% 42%, var(--peach-deep) 0 18%, var(--peach-mid) 34%, rgba(245,154,60,0.55) 52%, rgba(251,210,122,0) 70%),
      radial-gradient(ellipse at 40% 85%, var(--peach-light) 0 30%, rgba(251,210,122,0) 60%);
  }
  .brand-name {
    position: absolute;
    left: 211px;
    top: 72px;
    width: 132px;
    text-align: center;
    font-family: "Fredoka", Arial, sans-serif;
    font-weight: 600;
    font-size: 42px;
    line-height: 1;
    color: var(--brand-navy);
    letter-spacing: 0.5px;
  }
  .product-name {
    position: absolute;
    left: 149px;
    top: 140px;
    font-family: "Fredoka", Arial, sans-serif;
    font-weight: 600;
    font-size: 37px;
    line-height: 1;
    color: var(--brand-navy);
    white-space: nowrap;
  }
  .product-style {
    position: absolute;
    left: 150px;
    top: 180px;
    font-family: "Kaushan Script", cursive;
    font-size: 22px;
    line-height: 1;
    color: var(--brand-navy);
  }
  .product-name-fr {
    position: absolute;
    left: 147px;
    top: 223px;
    width: 260px;
    height: 36px;
    border-radius: 18px;
    background: var(--brand-navy);
    border: 2px solid var(--white);
    box-shadow: 0 0 0 2px var(--arch-yellow);
    color: var(--white);
    font-family: "Roboto", Arial, sans-serif;
    font-weight: 700;
    font-size: 23px;
    line-height: 32px;
    text-align: center;
  }
  .claim-badge {
    position: absolute;
    top: 289px;
    height: 36px;
    border-radius: 6px;
    background: var(--badge-green);
    border: 2px solid var(--white);
    color: var(--white);
    text-align: center;
    font-family: "Roboto", Arial, sans-serif;
    font-weight: 700;
    line-height: 1;
    padding-top: 4px;
  }
  .claim-badge .claim-main { display: block; font-size: 13px; }
  .claim-badge .claim-sub { display: block; font-size: 6px; margin-top: 3px; }
  .claim-badge--preservatives { left: 211px; width: 62px; }
  .claim-badge--natural { left: 277px; width: 62px; }
  .info-side {
    position: absolute;
    left: 913px;
    top: 0;
    width: 190px;
    height: 343px;
    color: var(--white);
  }
  .nutrition-title {
    position: absolute;
    left: 1px;
    top: 27px;
    font-size: 12px;
    font-weight: 700;
    white-space: nowrap;
  }
  .nutrition-panel {
    position: absolute;
    left: 0;
    top: 50px;
    width: 181px;
    height: 115px;
    background: var(--panel-grey);
  }
  .ingredients {
    position: absolute;
    left: 9px;
    top: 185px;
    font-size: 11.5px;
    font-weight: 500;
    line-height: 14px;
    white-space: nowrap;
  }
  .barcode-space {
    position: absolute;
    left: 4px;
    top: 246px;
    width: 176px;
    height: 74px;
    background: var(--panel-grey);
  }
</style>
</head>
<body>
<main class="canvas">
  <section class="label" aria-label="Peach halves in syrup jar label">
    <div class="front-arch"></div>
    <div class="peach-visual" role="img" aria-label="Ripe peach and peach half with a splash of golden syrup"></div>

    <div class="brand-name">MOLAN</div>
    <h1 class="product-name">Peach Halves</h1>
    <div class="product-style">in Syrup</div>
    <div class="product-name-fr">Pêches en moitiés</div>

    <div class="claim-badge claim-badge--preservatives">
      <span class="claim-main">NO ADDED</span>
      <span class="claim-sub">PRESERVATIVES</span>
    </div>
    <div class="claim-badge claim-badge--natural">
      <span class="claim-main">100%</span>
      <span class="claim-sub">NATURAL</span>
    </div>

    <div class="info-side">
      <p class="nutrition-title">panel for nutritional information</p>
      <div class="nutrition-panel"></div>
      <p class="ingredients">
        ingredients list<br>
        -Eng : peaches, water, Sugar.<br>
        -Fr : pêches, eau, sucre.
      </p>
      <div class="barcode-space"></div>
    </div>
  </section>
</main>
</body>
</html>
```